Tarrow Building Performance

Id like for my business card to be very bold and professional. Incorporating the business logo, the main services offered, and my contact info. Services are spray foam, insulation, new construction, retrofit, weatherization.

When opening this project sketch harbor was not able to upload my new logo that I picked from another recent sketch harbor project. Does anyone know how i could upload my logo onto the page for design of the business cards?

Target Market(s)

Building owners, contractors

Industry/Entity Type

Building Insulation and performance improvements

Contact Information for Business Card

Owner, Email dean@tarrowbuildingperformance.example Phone number 555-208-6147

Colors
0054AA
0677BA
7BADD7
CADEEF
E8F1F8
F0912C
F2A743
F7CA91
FBE8D2
FDF5EE

Requirements
Must have
• Services- spray foam, cellulose, mineral wool, fiberglass, air sealing, new construction, retrofit, weatherization, energy saving assesments

```html
<!DOCTYPE html>
<html lang="en">
<head>
<meta charset="utf-8">
<title>Tarrow Building Performance – Business Card</title>
<link href="https://fonts.googleapis.com/css2?family=Archivo:wght@400;700;800&family=Archivo+Narrow:wght@400;500&display=swap" rel="stylesheet">
<style>
  :root {
    --page: #e6e6e6;
    --navy: #0b1533;
    --navy-deep: #081029;
    --blue-pattern: #17306e;
    --orange: #f0812c;
    --sky: #3eb4e8;
    --white: #ffffff;
  }
  * { box-sizing: border-box; margin: 0; padding: 0; }
  html, body { width: 1200px; height: 1200px; overflow: hidden; }
  body {
    background: var(--page);
    font-family: "Archivo", Arial, sans-serif;
    position: relative;
  }
  .card {
    position: absolute;
    width: 689px;
    height: 393px;
    background: var(--navy);
    overflow: hidden;
  }
  .card--front { left: 267px; top: 159px; }
  .card--back { left: 262px; top: 653px; width: 688px; }

  .brand {
    position: absolute;
    left: 44px;
    top: 62px;
    color: var(--orange);
    font-weight: 800;
    text-transform: uppercase;
    line-height: 1;
  }
  .brand__line1 { font-size: 48px; letter-spacing: 1px; display: block; }
  .brand__line2 { font-size: 20px; letter-spacing: 0.5px; display: block; margin-top: 8px; }

  .person { position: absolute; left: 44px; top: 206px; }
  .person__name {
    color: var(--orange);
    font-weight: 700;
    font-size: 27px;
    letter-spacing: 0.5px;
  }
  .person__role {
    color: var(--sky);
    font-size: 16px;
    margin-top: 2px;
  }

  .contacts {
    position: absolute;
    left: 44px;
    top: 290px;
    list-style: none;
    color: var(--white);
    font-size: 16.5px;
    line-height: 21px;
  }
  .contacts li { display: flex; align-items: center; gap: 10px; }
  .contacts svg { width: 15px; height: 15px; flex: none; }

  .back-pattern {
    position: absolute;
    inset: 0;
    background: linear-gradient(90deg, var(--navy-deep) 0%, var(--navy) 45%, var(--blue-pattern) 100%);
    opacity: 0.9;
  }
  .back-mark {
    position: absolute;
    left: 357px;
    top: 222px;
    width: 141px;
    color: var(--orange);
    font-weight: 800;
    font-size: 40px;
    line-height: 1;
    text-align: center;
    letter-spacing: 1px;
  }
  .services {
    position: absolute;
    left: 20px;
    right: 20px;
    top: 285px;
    display: flex;
    align-items: center;
    justify-content: space-between;
    list-style: none;
    font-family: "Archivo Narrow", Arial, sans-serif;
    font-weight: 500;
    font-size: 17px;
    color: var(--white);
    text-transform: uppercase;
  }
  .services__dot { width: 9px; height: 9px; flex: none; }
</style>
</head>
<body>

<section class="card card--front">
  <div class="brand">
    <span class="brand__line1">Tarrow</span>
    <span class="brand__line2">Building Performance</span>
  </div>

  <div class="person">
    <h1 class="person__name">DEAN MARLOW</h1>
    <p class="person__role">Owner</p>
  </div>

  <ul class="contacts">
    <li>
      <svg viewBox="0 0 16 16" aria-hidden="true"><path fill="#f0812c" d="M3.5 1.5l2.5 0 1 3.5-1.6 1.2c.9 1.9 2.4 3.4 4.3 4.3L10.9 8.9l3.6 1v2.6c0 1-.8 1.8-1.8 1.6C7 13.3 2.7 9 1.9 3.3 1.7 2.3 2.5 1.5 3.5 1.5z"/></svg>
      555-208-6147
    </li>
    <li>
      <svg viewBox="0 0 16 16" aria-hidden="true"><rect x="1" y="3.5" width="14" height="9.5" fill="#f0812c"/><path d="M1.5 4l6.5 5 6.5-5" fill="none" stroke="#0b1533" stroke-width="1.3"/></svg>
      dean@tarrowbuildingperformance.example
    </li>
    <li>
      <svg viewBox="0 0 16 16" aria-hidden="true"><circle cx="8" cy="8" r="6.8" fill="#f0812c"/><path d="M4 5.5c1.5 0 2 1 3 1s1 2 0 2.5-1 2-.5 3M10 3.5c-.5 1 .5 2 1.5 2s1.5 1.5 1.5 2.5" fill="none" stroke="#0b1533" stroke-width="1.2"/></svg>
      www.tarrowbuildingperformance.example
    </li>
  </ul>
</section>

<section class="card card--back">
  <div class="back-pattern" role="img" aria-label="Faint repeating pattern of the company mark in navy to blue tones"></div>
  <div class="back-mark">TARROW</div>
  <ul class="services">
    <li>Spray Foam</li>
    <li><svg class="services__dot" viewBox="0 0 9 9" aria-hidden="true"><g fill="#3eb4e8"><rect width="4" height="4"/><rect x="5" width="4" height="4"/><rect y="5" width="4" height="4"/><rect x="5" y="5" width="4" height="4"/></g></svg></li>
    <li>Insulation</li>
    <li><svg class="services__dot" viewBox="0 0 9 9" aria-hidden="true"><g fill="#3eb4e8"><rect width="4" height="4"/><rect x="5" width="4" height="4"/><rect y="5" width="4" height="4"/><rect x="5" y="5" width="4" height="4"/></g></svg></li>
    <li>New Construction</li>
    <li><svg class="services__dot" viewBox="0 0 9 9" aria-hidden="true"><g fill="#3eb4e8"><rect width="4" height="4"/><rect x="5" width="4" height="4"/><rect y="5" width="4" height="4"/><rect x="5" y="5" width="4" height="4"/></g></svg></li>
    <li>Retrofit</li>
    <li><svg class="services__dot" viewBox="0 0 9 9" aria-hidden="true"><g fill="#3eb4e8"><rect width="4" height="4"/><rect x="5" width="4" height="4"/><rect y="5" width="4" height="4"/><rect x="5" y="5" width="4" height="4"/></g></svg></li>
    <li>Weatherization.</li>
  </ul>
</section>

</body>
</html>
```